Wordpress Design Papa Academy Project

Need a homepage design for a wordpress site that is based around becoming a better Dad. The sitemap file and logo file are attached. Navigation should be a combination of horizontal and vertical because the sitemap is extensive. I think the Father's conference, Daddy daughter dance and Essay contest would like nice if they were highlighted in their own rounded boxes at the bottom of the home page perhaps. New design needs to be attention grabbing, colorful but not over the top or too flashy either. I would like the background to be pictures and/or transparent words(similar to this site http://kinhelm.com/). Need a banner image which will be a slider and I need text overlay at the bottom of each image. I like rounded boxes like how this site showcases the news and events sections - http://www.qt.edu/. Need to also incorporate an events calendar, facebook and twitter icons and contact info. A preliminary design was initially created and is attached for you to review. Design needs to be balanced as there is alot of info to display.I have a current site here http://www.papaacad.com/ and you will see why I need a new design.
Updates

Target Market(s)

Dads

Industry/Entity Type

Events

Requirements
Must have
• image slider with text overlay on image, combination of horizontal and vertical navigation, show a dropdown menu under one of the horizontal tabs, events calendar, web safe fonts, colorful, use stock images for any placeholders,footer with sitemap
Nice to have
• rounded boxes, highlight father's conference,daddy daughter dance and essay contest in a separate section from the navigation, also put campus book store and online classes in a vertical nav bar perhaps - maybe in bigger placeholders like stacked boxes or similar.

```html
<!DOCTYPE html>
<html lang="en">
<head>
<meta charset="utf-8">
<title>Papa Academy, Inc.</title>
<link href="https://fonts.googleapis.com/css2?family=Arimo:wght@400;700&display=swap" rel="stylesheet">
<style>
:root{
  --blue:#1f5fae;
  --blue-dark:#164a8c;
  --blue-light:#3a7ccc;
  --heading:#1d4f91;
  --text:#333;
  --muted:#777;
  --page:#ececec;
  --panel:#f6f6f6;
  --frame:#6f6f6f;
  --footer:#3a3a3a;
  --footer-text:#d8d8d8;
  --cal-cell:#e6e6e6;
  --cal-today:#5aa0c8;
}
*{margin:0;padding:0;box-sizing:border-box}
html,body{width:812px;height:1200px;overflow:hidden}
body{position:relative;background:linear-gradient(#f3f3f3,#e9e9e9 900px,#eeeeee);font-family:Arimo,Arial,sans-serif;color:var(--text)}
.abs{position:absolute}
a{color:inherit;text-decoration:none}

/* header */
.brand{left:67px;top:17px;display:flex;align-items:center;gap:10px}
.brand-mark{width:48px;height:48px;border-radius:50%;background:var(--blue)}
.brand-name{font-size:20px;color:var(--heading);font-weight:400}
.social{display:flex;gap:6px}
.social span{width:19px;height:19px;border-radius:50%;background:var(--blue)}
.social.top{left:501px;top:25px}
.social.top span:last-child{background:#3fa6e0}
.toplinks{left:560px;top:30px;font-size:8.5px;color:#333;letter-spacing:.2px}
.toplinks i{font-style:normal;margin:0 5px;color:#888}

/* nav */
.mainnav{left:62px;top:76px;width:688px;height:29px;border-radius:4px 4px 0 0;background:linear-gradient(#3c82d2,#1c58a5);display:flex;color:#fff;font-size:9.5px}
.mainnav li{list-style:none;display:flex;align-items:center;justify-content:center;border-right:1px solid #1a4e93;box-shadow:1px 0 0 #4e8fd9}
.mainnav li.active{background:#174b8f}
.subbar{left:62px;top:105px;width:688px;height:39px;background:#fff;border:1px solid #ddd;border-top:0}
.search{left:83px;top:112px;width:125px;height:21px;border:1px solid #ccc;border-radius:2px;font-size:7.5px;color:#999;padding:6px 9px;background:#fff}
.search-btn{left:212px;top:113px;width:43px;height:19px;background:linear-gradient(#8a8a8a,#5e5e5e);color:#fff;font-size:7.5px;text-align:center;line-height:19px;border-radius:2px}
.sublinks{left:450px;top:105px;height:39px;display:flex;font-size:9px;color:#555}
.sublinks span{display:flex;align-items:center;padding:0 8px;border-left:1px solid #ddd;height:39px}
.sublinks span+span{padding:0 15px 0 24px}

/* slider */
.slider{left:66px;top:153px;width:680px;height:193px;background:var(--frame);border-radius:3px}
.slide{left:70px;top:157px;width:488px;height:185px;background:linear-gradient(100deg,#c9a98c 0%,#b88f73 25%,#e2dad2 48%,#f1efec 70%)}
.slide-text{left:70px;top:173px;width:479px;text-align:right;font-size:12.5px;color:#111;line-height:21px}
.slide-text strong{display:block;font-weight:400;font-size:14.5px;color:var(--blue);margin-top:6px;letter-spacing:.3px}
.dots{left:490px;top:316px;display:flex;gap:7px}
.dots span{width:7px;height:7px;border-radius:50%;background:#999}
.dots span:first-child{background:var(--blue)}
.events-title{left:572px;top:168px;color:#fff;font-size:13.5px;letter-spacing:.3px}
.cal{left:572px;top:190px;width:149px;background:#fff;font-size:8px;color:#333}
.cal-head{height:22px;background:#3e3e3e;color:#fff;display:flex;justify-content:space-between;align-items:center;padding:0 7px;font-size:9px}
.cal-days,.cal-row{display:grid;grid-template-columns:repeat(7,1fr)}
.cal-days span{font-size:5.5px;text-align:center;padding:3px 0;color:#444}
.cal-row span{height:20px;margin:1px;background:var(--cal-cell);display:flex;align-items:center;justify-content:center}
.cal-row .off{color:#aaa;background:#efefef}
.cal-row .today{background:var(--cal-today);color:#fff}

/* welcome */
.welcome{left:67px;top:370px;width:480px}
.section-title{font-size:13px;color:var(--heading);font-weight:400;letter-spacing:.2px}
.welcome p{font-size:8px;line-height:16.3px;margin-top:10px;color:#222}
.welcome p+p{margin-top:16px}
.classes{left:565px;top:359px;width:181px;height:191px;background:linear-gradient(#3a78c4,#2a60a8);border-radius:3px;color:#fff}
.classes h3{font-size:13px;font-weight:400;padding:11px 0 0 14px}
.video{left:11px;top:32px;width:161px;height:113px;background:linear-gradient(#5a2020,#2a1010);border:2px solid #dfe6ee}
.video-bar{left:0;bottom:0;width:100%;height:11px;background:#1b1b1b}
.play{left:66px;top:45px;width:26px;height:20px;background:#222;border-radius:3px}
.classes p{left:22px;top:153px;font-size:8px;line-height:12px;color:#e6eef8;width:150px}

/* tabs */
.tabs{left:66px;top:578px;display:flex;gap:12px}
.tabs span{height:30px;border-radius:10px 10px 0 0;background:#f3f3f3;font-size:9.5px;color:#333;display:flex;align-items:center;padding:0 15px 0 19px;min-width:140px}
.tabs span.on{background:#e6e6e6;color:var(--blue)}
.tab-panel{left:66px;top:608px;width:680px;height:148px;background:#e6e6e6}
.tab-inner{left:72px;top:614px;width:668px;height:136px;background:#fff}
.tab-photo{left:84px;top:626px;width:201px;height:110px;background:linear-gradient(120deg,#6b4a34,#9a7a5e 40%,#c9b9a4 70%,#4d3a2c);border:3px solid #e3e3e3}
.tab-copy{left:303px;top:622px;width:422px;font-size:8px;line-height:15.6px;color:#222}
.tab-copy p+p{margin-top:6px}
.tab-copy a{display:block;color:var(--blue);margin-top:4px}

/* products */
.promo-title{top:776px;font-size:11.5px;font-weight:400;color:var(--heading)}
.promo{top:796px;width:216px;height:100px;background:linear-gradient(#2b65af,#1e5398);border-radius:2px}
.promo-img{left:6px;top:6px;width:113px;height:85px;background:#fff;display:flex;align-items:center;justify-content:center}
.promo-img i{display:block;width:60px;height:66px;border-radius:8px}
.promo p{left:126px;top:16px;width:85px;font-size:8px;line-height:12.8px;color:#fff}
.promo-btn{left:126px;top:62px;width:80px;height:21px;border-radius:10px;background:linear-gradient(#fff,#e4e4e4);color:#444;font-size:9px;display:flex;align-items:center;justify-content:center}

.contact{left:0;top:925px;width:812px;text-align:center;font-size:15px;color:#444}
.contact span{margin:0 22px}
.contact svg{vertical-align:-2px;margin-right:6px}

/* footer */
.footer{left:0;top:960px;width:812px;height:240px;background:linear-gradient(#444,#2e2e2e);border-top:2px solid #d5d5d5}
.fcol{top:985px;list-style:none;font-size:7.5px;color:var(--footer-text)}
.fcol li{height:18.4px}
.fcol li::before{content:"•";margin-right:5px}
.fdivider{left:66px;top:1133px;width:680px;height:1px;background:#555}
.copyright{left:68px;top:1160px;font-size:9px;color:#bbb;word-spacing:1px}
.social.bottom{left:698px;top:1155px}
.social.bottom span{background:#777}
</style>
</head>
<body>

<header>
  <div class="abs brand"><span class="brand-mark"></span><span class="brand-name">Papa Academy, Inc.</span></div>
  <div class="abs social top"><span></span><span></span></div>
  <div class="abs toplinks">CONTACT<i>|</i>AFFILIATIONS<i>|</i>MESSAGE BOARD</div>
</header>

<nav>
  <ul class="abs mainnav">
    <li style="width:48px"><svg width="11" height="10" viewBox="0 0 11 10"><path d="M5.5 0L0 5h1.5v5h3V7h2v3h3V5H11z" fill="#fff"/></svg></li>
    <li style="width:56px">About</li>
    <li style="width:62px">Contact</li>
    <li style="width:77px">Admissions</li>
    <li style="width:80px">Information</li>
    <li style="width:65px">Services</li>
    <li class="active" style="width:69px">Products</li>
    <li style="width:118px">Fathers Conference</li>
    <li style="width:52px">Help</li>
    <li style="width:61px;border:0;box-shadow:none">FAQ</li>
  </ul>
  <div class="abs subbar"></div>
  <div class="abs search">Enter key word...</div>
  <div class="abs search-btn">SEARCH</div>
  <div class="abs sublinks"><span>My Hero / My Dad Essay Contest</span><span>Daddy Daughter Dance</span></div>
</nav>

<section>
  <div class="abs slider"></div>
  <div class="abs slide" role="img" aria-label="Photo of a father holding his young daughter while using a tablet"></div>
  <div class="abs slide-text">we are helping to all fathers appreciate themselves<br>and the responsibility of fatherhood.<strong>GREATEST RESPONSIBILITY</strong></div>
  <div class="abs dots"><span></span><span></span><span></span><span></span></div>
  <div class="abs events-title">UPCOMING EVENTS</div>
  <div class="abs cal">
    <div class="cal-head"><span>◂</span><span>November&nbsp; 2012</span><span>▸</span></div>
    <div class="cal-days"><span>MON</span><span>TUE</span><span>WED</span><span>THU</span><span>FRI</span><span>SAT</span><span>SUN</span></div>
    <div class="cal-row"><span class="off">28</span><span>1</span><span>2</span><span>3</span><span class="today">4</span><span>5</span><span>6</span></div>
    <div class="cal-row"><span>7</span><span>8</span><span>9</span><span>10</span><span>11</span><span>12</span><span>13</span></div>
    <div class="cal-row"><span>14</span><span>15</span><span>16</span><span>17</span><span>18</span><span>19</span><span>20</span></div>
    <div class="cal-row"><span>21</span><span>22</span><span>23</span><span>24</span><span>25</span><span>26</span><span>27</span></div>
    <div class="cal-row"><span>28</span><span>29</span><span>30</span><span>31</span><span class="off">1</span><span class="off">2</span><span class="off">3</span></div>
  </div>
</section>

<section class="abs welcome">
  <h2 class="section-title">WELCOME TO OUR SITE</h2>
  <p>Papa Academy is dedicated to helping all fathers appreciate themselves and the responsibility of fatherhood. We cater to soon to be fathers, new fathers, existing fathers, and second time parents. As Fathers we find ourselves in a strange situation, sometimes not knowing what is right, what is best, or what to say. But we are always, always looked to as leaders. In this situation, we must band together to help one another with the greatest responsibility of all, the rise or demise of the next generation.</p>
  <p>Our goal is simply, to heal the world one father and child at a time. Our plan is to use all available resources to create a one-stop site for fatherhood. By helping them understand the importance their role has on the future of children throughout the world. We can bring them closer to their families through educating them on pregnancy, maternity, child bearing, and quality time which will help produce a strong minded, loved, and whole child. Where leaders come to learn!</p>
</section>

<aside class="abs classes">
  <h3>ONLINE CLASSES</h3>
  <div class="abs video" role="img" aria-label="Video still of an instructor speaking to camera">
    <div class="abs play"><svg width="26" height="20" viewBox="0 0 26 20"><path d="M10 5l8 5-8 5z" fill="#fff"/></svg></div>
    <div class="abs video-bar"></div>
  </div>
  <p class="abs">Aqui dolorem ipsum quia dolor amet, consectetur.</p>
</aside>

<section>
  <div class="abs tabs">
    <span class="on">FATHER'S CONFERENCE</span><span style="min-width:117px">ESSAY CONTEST</span><span style="min-width:161px">DADDY DAUGHTER DANCE</span><span>BEST FATHER</span>
  </div>
  <div class="abs tab-panel"></div>
  <div class="abs tab-inner"></div>
  <div class="abs tab-photo" role="img" aria-label="Photo of fathers seated and taking notes at a conference"></div>
  <div class="abs tab-copy">
    <p>Sed ut perspiciatis unde omnis iste natus error sit voluptatem accusantium doloremque laudantium, totam rem aperiam, eaque ipsa quae ab illo inventore veritatis et quasi architecto beatae vitae dicta sunt explicabo. Nemo enim ipsam voluptatem quia voluptas sit aspernatur aut odit aut fugit, sed quia consequuntur magni dolores eos qui ratione voluptatem sequi nesciunt.</p>
    <p>Neque porro quisquam est, qui dolorem ipsum quia dolor sit amet, consectetur, adipisci velit, sed quia non numquam eius modi tempora incidunt ut labore et dolore magnam aliquam.</p>
    <a>VIEW MORE</a>
  </div>
</section>

<section>
  <h3 class="abs promo-title" style="left:66px">THE DADDY STORE</h3>
  <h3 class="abs promo-title" style="left:298px">DADDY GIFT SHOP</h3>
  <h3 class="abs promo-title" style="left:530px">THE DADDY BAG</h3>

  <div class="abs promo" style="left:66px">
    <div class="abs promo-img"><i role="img" aria-label="Photo of a tan leather backpack" style="background:linear-gradient(#d9a04a,#a8701f)"></i></div>
    <p class="abs">Quis autem vel eum iure reprehenderit qui in ea voluptate.</p>
    <div class="abs promo-btn">VIEW MORE</div>
  </div>
  <div class="abs promo" style="left:298px">
    <div class="abs promo-img"><i role="img" aria-label="Illustration of a June calendar page with a heart and gift box" style="background:linear-gradient(135deg,#eeeeee 40%,#2f7fe0 40%)"></i></div>
    <p class="abs">Quis autem vel eum iure reprehenderit qui in ea voluptate.</p>
    <div class="abs promo-btn">VIEW MORE</div>
  </div>
  <div class="abs promo" style="left:530px">
    <div class="abs promo-img"><i role="img" aria-label="Photo of a navy and white backpack" style="background:linear-gradient(90deg,#2a2f4a,#d8d8e0 50%,#2a2f4a)"></i></div>
    <p class="abs">Quis autem vel eum iure reprehenderit qui in ea voluptate.</p>
    <div class="abs promo-btn">VIEW MORE</div>
  </div>
</section>

<div class="abs contact">
  <span><svg width="14" height="14" viewBox="0 0 14 14"><path d="M3 1l2 3-1.3 1.3a8 8 0 0 0 5 5L10 9l3 2-1.5 2.5C6 13 1 8 .8 2.5z" fill="#666"/></svg>Call us : &nbsp;555 214 7390</span>|<span><svg width="14" height="12" viewBox="0 0 14 12"><path d="M1 5l6-4 6 4v6H1z M1 5l6 4 6-4" fill="none" stroke="#666" stroke-width="1.4"/></svg>Email : &nbsp;info@papaacad.com</span>
</div>

<footer>
  <div class="abs footer"></div>
  <ul class="abs fcol" style="left:66px"><li>HOME</li><li>ABOUT US</li><li>CONTACT</li><li>ADMISSIONS</li><li>INFORMATION</li><li>SERVICES</li><li>PRODUCTS</li></ul>
  <ul class="abs fcol" style="left:177px"><li>FATHERS CONFERENCE</li><li>MY HERO / MY DAD ESSAY CONTEST</li><li>DADDY DAUGHTER DANCE</li><li>ONLINE COURSES</li><li>BLOG</li></ul>
  <ul class="abs fcol" style="left:373px"><li>HOME</li><li>ABOUT US</li><li>CONTACT</li><li>ADMISSIONS</li><li>INFORMATION</li><li>SERVICES</li><li>PRODUCTS</li></ul>
  <ul class="abs fcol" style="left:484px"><li>FATHERS CONFERENCE</li><li>MY HERO / MY DAD ESSAY CONTEST</li><li>DADDY DAUGHTER DANCE</li><li>ONLINE COURSES</li><li>BLOG</li></ul>
  <ul class="abs fcol" style="left:681px"><li>HOME</li><li>ABOUT US</li><li>CONTACT</li><li>ADMISSIONS</li><li>INFORMATION</li><li>SERVICES</li><li>PRODUCTS</li></ul>
  <div class="abs fdivider"></div>
  <div class="abs copyright">Copyright © 2012 &nbsp;www.papaacad.com &nbsp;&nbsp;All rights reserved.</div>
  <div class="abs social bottom"><span></span><span></span></div>
</footer>

</body>
</html>
```